Business Card design for a skin clinic

i would like a business card design for our skin clinic.
our logo colors are Blue and Grey and Bule /white.
we are searching for a minimalistic design yet very elegant,dynamic and professional which can reflect a professional medical skin care clinic( not a beauty salon).
THE DESGIN IS NOT FOR A PERSON IT WILL BE USED IN THE CLINIC FOR CLIENTS SO THERE SHOULD BE NO NAME OF A PERSON ONLY THE CLINIC NAME AND THE CONTACT INFO

Target Market(s)
young and old womens
Industry/Entity Type
Business
Contact Information for Business Card
we have 2 address and both should be on the card.
address A: Lindenhoflaan 214B, 3041KP Rotterdam, Tel 010 483 21 95
address B: Zonnewijzerstraat 238, 1062RT Amsterdam Tel 020 571 3829
website www.huidpuntzorg.nu, email info@huidpuntzorg.nu
Look and feel
Each slider illustrates characteristics of the customer's brand and the style your logo design should communicate.

```html
<!DOCTYPE html>
<html lang="nl">
<head>
<meta charset="utf-8">
<title>Huidpuntzorg – visitekaartje</title>
<link href="https://fonts.googleapis.com/css2?family=Jost:wght@400;500;600&display=swap" rel="stylesheet">
<style>
  :root {
    --canvas: #efebe6;
    --card-front: #e1f2f9;
    --card-back: #b9e6f3;
    --brand-blue: #2ba3dc;
    --brand-grey: #6e6f71;
    --pattern-tint: #9fd8ec;
  }
  * { margin: 0; padding: 0; box-sizing: border-box; }
  html, body { width: 1200px; height: 648px; overflow: hidden; }
  body {
    background: var(--canvas);
    font-family: "Jost", "Futura", sans-serif;
    position: relative;
  }
  .card {
    position: absolute;
    top: 175px;
    width: 520px;
    height: 297px;
    border-radius: 3px;
    box-shadow: 0 6px 18px rgba(80, 70, 60, 0.16);
    overflow: hidden;
  }
  .card--front { left: 60px; background: var(--card-front); }
  .card--back { left: 620px; background: var(--card-back); }

  .corner-motif {
    position: absolute;
    width: 70px;
    height: 46px;
    background: var(--pattern-tint);
    opacity: 0.7;
  }
  .corner-motif--top-left { top: 0; left: 0; border-bottom-right-radius: 28px; }
  .corner-motif--bottom-right { bottom: 0; right: 0; width: 78px; height: 58px; border-top-left-radius: 30px; }

  .brand {
    position: absolute;
    top: 44px;
    left: 250px;
    display: flex;
    align-items: center;
    gap: 10px;
  }
  .brand-dot {
    width: 14px; height: 14px;
    border-radius: 50%;
    background: var(--brand-blue);
  }
  .brand-name {
    font-size: 27px;
    font-weight: 500;
    letter-spacing: 2px;
    color: var(--brand-grey);
  }

  .address {
    position: absolute;
    font-size: 17px;
    line-height: 1.22;
    color: var(--brand-grey);
  }
  .address .street { color: var(--brand-blue); }
  .address .tel-label { color: var(--brand-blue); font-weight: 600; margin-right: 4px; }
  .address--rotterdam { top: 40px; left: 44px; }
  .address--amsterdam { top: 185px; left: 270px; }

  .divider {
    position: absolute;
    left: 250px;
    top: 150px;
    width: 1.5px;
    height: 70px;
    background: var(--brand-blue);
  }

  .online {
    position: absolute;
    top: 195px;
    left: 60px;
    text-align: right;
    width: 170px;
    font-size: 16px;
    line-height: 1.25;
    color: var(--brand-grey);
  }

  .back-pattern {
    position: absolute;
    inset: 0;
    background: linear-gradient(135deg, #b4e3f2 0%, #a6dcef 50%, #b9e6f3 100%);
  }
</style>
</head>
<body>
  <section class="card card--front" aria-label="Voorkant visitekaartje">
    <div class="corner-motif corner-motif--top-left" role="img" aria-label="Decoratief druppelpatroon in blauw en grijs"></div>
    <div class="corner-motif corner-motif--bottom-right" role="img" aria-label="Decoratief druppelpatroon in blauw en grijs"></div>

    <div class="address address--rotterdam">
      <p class="street">Lindenhoflaan 214B</p>
      <p>3041KP Rotterdam</p>
      <p><span class="tel-label">Tel</span>010 483 21 95</p>
    </div>

    <div class="brand">
      <span class="brand-dot"></span>
      <span class="brand-name">HUIDPUNTZORG</span>
    </div>

    <div class="divider"></div>

    <div class="online">
      <p>www.huidpuntzorg.nu</p>
      <p>info@huidpuntzorg.nu</p>
    </div>

    <div class="address address--amsterdam">
      <p class="street">Zonnewijzerstraat 238</p>
      <p>1062RT Amsterdam</p>
      <p><span class="tel-label">Tel</span>020 571 3829</p>
    </div>
  </section>

  <section class="card card--back" aria-label="Achterkant visitekaartje">
    <div class="back-pattern" role="img" aria-label="Herhalend patroon van blauwe en grijze druppelvormen over de hele achterkant"></div>
  </section>
</body>
</html>
```